Corvelle Matchmaking - Innovative AI-based Online Dating App

Hello, I am creating a new online dating app that subsumes the personalization and compatibility analysis of human matchmaking, but is combined with the convenience of modern dating apps such as brisket. The app is called Corvelle.

There is a lot of pain and fatigue in modern online dating. Corvelle uses a concise but effective questionnaire that is combined with cutting-edge AI, social psychology research, and psycholinguistic modelling to effectively and conveniently find dating matches with real compatibility - as opposed to any major app on the market. A personalized introduction for every user is generated everyday to introduce you to a new potential match - this introduction is totally unique and will never be seen before or again. The introduction is intertwined with the user’s images to create an attractive “newsletter” feel.

"Corvelle" is Italian for lagoon, which is "a shallow body of water protected from a larger body of water (usually the ocean) by sandbars, barrier islands, or coral reefs." Lagoons are beautiful, tropical, lush watery paradises - as I see it. This is meant to be the inspiration for the feel, color scheme and design of the app.

To that end, I have included concept images of lagoons to evoke the feeling of a paradise getaway where one may meet their soulmate. This is the feeling I would like to convey with the minimalist app design this product needs to compete.

I have included screenshots of the current app UI. There is a screen for
1) potential matches and incoming likes (just like Brisket) with a logo at the top. There are “Like”, “Dislike”, “Super Like”, and “Super Dislike” buttons that float over the screen as it scrolls. These button shape/colors likely need to change to match the rest of the design
2) Overview of message threads with each match
3) View of message threads
4) Settings page

I would like
1) the logo/header image to be redone (as well as the like/dislike/super like/super dislike buttons to be redone to match the new design)
2) icons for the 4 pages in the bottom navigation bar to be redone
3) color scheme to be optimized and evoking of the desired paradise but professional feeling of a hyper-intelligent (but also empathetic) matchmaker
4) design for the settings screen (to look professional and competitive with other dating apps)

The color scheme /layout/spacing/font(s) for the bubbles on the screen where new potential matches are introduced is the most important part of the design I’m looking for. It’s currently a stack of rounded rectangles basically, but I’m open to all ideas to make this app look as professional as possible while conveying the desired elegance, empathy, and uniqueness of the brand.

Thank you!

Target Market(s)

Single men and women ages 20 - 45

Industry/Entity Type

Online dating / Matchmaking

Requirements
Must have
• For the main screen where new users are being introduced (i.e. the "swipe" page on most dating apps) - some amount of matchmaking introductory text MUST be shown above the user's first profile picture, as indicated in the current screenshots.
Nice to have
• Re-designs of the top "Corvelle" logo/emblem would be nice. If changing the logo, some emblem or graphic in addition to just the text of "Corvelle" would be nice. (Like the way "plumway" has its red flame emblem)
Should not have
• The main "swipe" page should not look identical to other dating apps in the sense of being >90% just a user's first dating profile image. The competitive edge to this app is the user-to-user specific matchmaking introductory text, so some of that must be visible before a user scrolls down for further profile information.

```html
<!DOCTYPE html>
<html lang="en">
<head>
<meta charset="utf-8">
<title>Corvelle – Messages</title>
<link href="https://fonts.googleapis.com/css2?family=Poppins:wght@400;500;600&display=swap" rel="stylesheet">
<style>
:root{
  --ink:#1b2a4e;
  --muted:#5d6478;
  --icon:#7a8196;
  --mint:#2fdcaa;
  --mint-light:#5ef0c6;
  --mint-wash:#a9f0d6;
  --pink:#f0356f;
  --white:#ffffff;
}
*{margin:0;padding:0;box-sizing:border-box}
html,body{width:1200px;height:2598px;overflow:hidden}
body{
  font-family:"Poppins",sans-serif;
  background:
    radial-gradient(ellipse 700px 560px at 0 0, var(--mint-wash) 0%, rgba(169,240,214,.35) 45%, rgba(255,255,255,0) 100%),
    var(--white);
  position:relative;
  color:var(--ink);
}
.status-bar{position:absolute;top:56px;left:50px;right:64px;height:52px;display:flex;justify-content:space-between;align-items:center}
.status-time{font-size:37px;font-weight:500;color:#555c6b}
.status-icons{display:flex;gap:14px;align-items:center}

.bell-button{position:absolute;left:51px;top:181px;width:114px;height:114px;border-radius:50%;background:var(--white);box-shadow:0 10px 30px rgba(40,80,70,.08);display:flex;align-items:center;justify-content:center}
.brand{position:absolute;left:0;right:0;top:200px;display:flex;justify-content:center;align-items:center;gap:16px}
.brand-dot{width:34px;height:34px;border-radius:50%;background:var(--mint)}
.brand-name{font-size:56px;font-weight:600;color:var(--ink);letter-spacing:1px}
.menu-button{position:absolute;left:1050px;top:214px}

.search-row{position:absolute;top:365px;left:63px;right:74px;height:126px}
.search-box{position:absolute;left:0;width:730px;height:126px;border-radius:30px;background:var(--white);box-shadow:0 12px 36px rgba(30,50,80,.07);display:flex;align-items:center;padding:0 48px;justify-content:space-between}
.search-placeholder{font-size:37px;color:#7d8395}
.tool-button{position:absolute;top:0;width:126px;height:126px;border-radius:30px;background:var(--white);box-shadow:0 12px 36px rgba(30,50,80,.07);display:flex;align-items:center;justify-content:center}
.tool-filter{left:778px}
.tool-adjust{left:937px}

.thread-list{position:absolute;top:555px;left:63px;right:70px;list-style:none}
.thread{position:relative;height:206px}
.avatar{position:absolute;left:0;top:0;width:140px;height:140px;border-radius:50%}
.thread-name{position:absolute;left:173px;top:2px;font-size:44px;font-weight:600;color:var(--ink)}
.thread-preview{position:absolute;left:173px;top:84px;font-size:37px;color:var(--muted)}
.unread-dot{position:absolute;left:931px;top:61px;width:18px;height:18px;border-radius:50%;background:var(--pink);box-shadow:0 4px 14px rgba(240,53,111,.45)}
.thread-more{position:absolute;left:1028px;top:42px;display:flex;flex-direction:column;gap:15px}
.thread-more span{width:13px;height:13px;border-radius:50%;background:var(--icon)}

.tab-bar{position:absolute;left:0;right:0;top:2358px;height:140px}
.tab{position:absolute;top:0;height:140px;display:flex;align-items:center;justify-content:center}
.tab-active{left:667px;width:139px;border-radius:32px;background:linear-gradient(160deg,var(--mint-light),var(--mint));box-shadow:0 18px 40px rgba(47,220,170,.45)}
</style>
</head>
<body>

<div class="status-bar">
  <span class="status-time">9:41</span>
  <div class="status-icons">
    <svg width="56" height="36" viewBox="0 0 56 36"><g fill="#555c6b"><rect x="0" y="24" width="10" height="12" rx="2"/><rect x="15" y="16" width="10" height="20" rx="2"/><rect x="30" y="8" width="10" height="28" rx="2"/><rect x="45" y="0" width="10" height="36" rx="2"/></g></svg>
    <svg width="50" height="38" viewBox="0 0 50 38"><g fill="none" stroke="#555c6b" stroke-width="6" stroke-linecap="round"><path d="M4 12 A30 30 0 0 1 46 12"/><path d="M12 21 A18 18 0 0 1 38 21"/></g><circle cx="25" cy="32" r="5" fill="#555c6b"/></svg>
    <svg width="78" height="40" viewBox="0 0 78 40"><rect x="2" y="2" width="66" height="36" rx="10" fill="none" stroke="#555c6b" stroke-width="3"/><rect x="7" y="7" width="56" height="26" rx="6" fill="#555c6b"/><rect x="71" y="13" width="5" height="14" rx="2" fill="#555c6b"/></svg>
  </div>
</div>

<header>
  <div class="bell-button">
    <svg width="60" height="64" viewBox="0 0 60 64"><path d="M30 6c-11 0-19 9-19 20v13l-6 8h50l-6-8V26C49 15 41 6 30 6z" fill="var(--mint)"/><path d="M24 52a6 6 0 0 0 12 0z" fill="var(--mint)"/><circle cx="47" cy="10" r="8" fill="var(--ink)" stroke="#fff" stroke-width="3"/></svg>
  </div>
  <div class="brand">
    <span class="brand-dot"></span>
    <span class="brand-name">Corvelle</span>
  </div>
  <div class="menu-button">
    <svg width="64" height="48" viewBox="0 0 64 48"><g stroke="var(--ink)" stroke-width="6" stroke-linecap="round"><line x1="14" y1="4" x2="61" y2="4"/><line x1="3" y1="24" x2="61" y2="24"/><line x1="24" y1="44" x2="61" y2="44"/></g></svg>
  </div>
</header>

<div class="search-row">
  <div class="search-box">
    <span class="search-placeholder">Search User...</span>
    <svg width="54" height="54" viewBox="0 0 54 54"><circle cx="24" cy="24" r="20" fill="none" stroke="var(--icon)" stroke-width="4"/><line x1="39" y1="39" x2="51" y2="51" stroke="var(--icon)" stroke-width="4" stroke-linecap="round"/></svg>
  </div>
  <div class="tool-button tool-filter">
    <svg width="56" height="50" viewBox="0 0 56 50"><path d="M4 4h48L33 26v18l-10-5V26z" fill="none" stroke="var(--icon)" stroke-width="4" stroke-linejoin="round"/></svg>
  </div>
  <div class="tool-button tool-adjust">
    <svg width="54" height="48" viewBox="0 0 54 48"><g stroke="var(--icon)" stroke-width="4" stroke-linecap="round"><line x1="8" y1="4" x2="8" y2="44"/><line x1="27" y1="4" x2="27" y2="44"/><line x1="46" y1="4" x2="46" y2="44"/><line x1="1" y1="30" x2="15" y2="30"/><line x1="20" y1="14" x2="34" y2="14"/><line x1="39" y1="32" x2="53" y2="32"/></g></svg>
  </div>
</div>

<ul class="thread-list">
  <li class="thread"><div class="avatar" role="img" aria-label="Profile photo of Marisol Venturi" style="background:linear-gradient(135deg,#9fb9c6,#8a4a32)"></div><span class="thread-name">Marisol Venturi</span><span class="thread-preview">Message would be here.</span><div class="thread-more"><span></span><span></span><span></span></div></li>
  <li class="thread"><div class="avatar" role="img" aria-label="Profile photo of Ines Dorval" style="background:linear-gradient(135deg,#8f7c66,#c9a27a)"></div><span class="thread-name">Ines Dorval</span><span class="thread-preview">Message would be here.</span><span class="unread-dot"></span><div class="thread-more"><span></span><span></span><span></span></div></li>
  <li class="thread"><div class="avatar" role="img" aria-label="Profile photo of Talia Brennock" style="background:linear-gradient(135deg,#3a3230,#d8cfc8)"></div><span class="thread-name">Talia Brennock</span><span class="thread-preview">Message would be here.</span><div class="thread-more"><span></span><span></span><span></span></div></li>
  <li class="thread"><div class="avatar" role="img" aria-label="Profile photo of Nora Vellis" style="background:linear-gradient(135deg,#d9d2c8,#7a4a30)"></div><span class="thread-name">Nora Vellis</span><span class="thread-preview">Message would be here.</span><span class="unread-dot"></span><div class="thread-more"><span></span><span></span><span></span></div></li>
  <li class="thread"><div class="avatar" role="img" aria-label="Profile photo of Priya Kestrel" style="background:linear-gradient(135deg,#5a3318,#d9a066)"></div><span class="thread-name">Priya Kestrel</span><span class="thread-preview">Message would be here.</span><div class="thread-more"><span></span><span></span><span></span></div></li>
  <li class="thread"><div class="avatar" role="img" aria-label="Profile photo of Lena Hartwick" style="background:linear-gradient(135deg,#2c2b2a,#8a7060)"></div><span class="thread-name">Lena Hartwick</span><span class="thread-preview">Message would be here.</span><div class="thread-more"><span></span><span></span><span></span></div></li>
  <li class="thread"><div class="avatar" role="img" aria-label="Profile photo of Sienna Marlow" style="background:linear-gradient(135deg,#d8d2cc,#a0806a)"></div><span class="thread-name">Sienna Marlow</span><span class="thread-preview">Message would be here.</span><span class="unread-dot"></span><div class="thread-more"><span></span><span></span><span></span></div></li>
  <li class="thread"><div class="avatar" role="img" aria-label="Profile photo of Elise Varden" style="background:linear-gradient(135deg,#b7aea6,#2e2420)"></div><span class="thread-name">Elise Varden</span><span class="thread-preview">Message would be here.</span><div class="thread-more"><span></span><span></span><span></span></div></li>
  <li class="thread"><div class="avatar" role="img" aria-label="Profile photo of Ruby Callan" style="background:linear-gradient(135deg,#3fb7c9,#c8243c)"></div><span class="thread-name">Ruby Callan</span><span class="thread-preview">Message would be here.</span><div class="thread-more"><span></span><span></span><span></span></div></li>
</ul>

<nav class="tab-bar">
  <div class="tab" style="left:125px;width:80px">
    <svg width="68" height="68" viewBox="0 0 68 68"><g fill="none" stroke="var(--icon)" stroke-width="8" stroke-linecap="round"><path d="M10 30A25 25 0 0 1 55 20"/><path d="M58 38A25 25 0 0 1 13 48"/></g><path d="M60 6v20H40z" fill="var(--icon)"/><path d="M8 62V42h20z" fill="var(--icon)"/></svg>
  </div>
  <div class="tab" style="left:411px;width:80px">
    <svg width="66" height="64" viewBox="0 0 66 64"><path d="M4 28L33 4l29 24v30a6 6 0 0 1-6 6H10a6 6 0 0 1-6-6z" fill="var(--icon)" stroke="var(--icon)" stroke-width="4" stroke-linejoin="round"/><line x1="24" y1="54" x2="42" y2="54" stroke="#fff" stroke-width="4" stroke-linecap="round"/></svg>
  </div>
  <div class="tab tab-active">
    <svg width="68" height="66" viewBox="0 0 68 66"><path d="M10 10h44a8 8 0 0 1 8 8v26a8 8 0 0 1-8 8H40l-10 12-6-12H10a8 8 0 0 1-8-8V18a8 8 0 0 1 8-8z" fill="#fff"/><g fill="var(--mint)"><circle cx="20" cy="31" r="4"/><circle cx="32" cy="31" r="4"/><circle cx="44" cy="31" r="4"/></g><circle cx="58" cy="8" r="8" fill="#fff" stroke="var(--mint)" stroke-width="3"/></svg>
  </div>
  <div class="tab" style="left:985px;width:80px">
    <svg width="60" height="64" viewBox="0 0 60 64"><circle cx="30" cy="18" r="16" fill="var(--icon)"/><path d="M2 62c0-16 12-26 28-26s28 10 28 26z" fill="var(--icon)"/></svg>
  </div>
</nav>

</body>
</html>
```